New business card/stationary for a consulting company

I am looking for a clean and very professional looking business card for my consulting company as well as corresponding stationary. I am uploading our logo. I like simple and powerful for the feel. No graphics but I am open on everything else. Below is my contact information but would like the final to be in a version I can add my employees information into and print. Thank you.

Daniel Whitcombe
dan@fernlowadvisory.com
2837 North 9th Avenue, Summit Floor, Cedar Hollow, Westland 60483
www.fernlowadvisory.com

Industry/Entity Type

Consulting

Contact Information for Business Card

Daniel Whitcombe
dan@fernlowadvisory.com
www.fernlowadvisory.com

Font styles to use
Serif
Sans Serif

Requirements
Must have
• Our logo and the business card details.
Nice to have
• our website www.fernlowadvisory.com

```html
<!DOCTYPE html>
<html lang="en">
<head>
<meta charset="utf-8">
<title>Fernlow Advisory — Business Card</title>
<link rel="stylesheet" href="https://fonts.googleapis.com/css2?family=Cinzel:wght@400&family=Questrial&family=Libre+Baskerville:wght@400&display=swap">
<style>
  :root {
    --navy: #0c0c63;
    --ink: #141414;
    --paper: #fefefe;
    --page: #ffffff;
    --edge: #8a8a8a;
  }
  html, body {
    margin: 0;
    padding: 0;
    width: 1200px;
    height: 1200px;
    overflow: hidden;
    background: var(--page);
  }
  .canvas {
    position: relative;
    width: 1200px;
    height: 1200px;
  }
  .card {
    position: absolute;
    left: 122px;
    top: 320px;
    width: 956px;
    height: 559px;
    background: var(--paper);
    border: 1px solid var(--edge);
    box-sizing: border-box;
  }
  .brand-mark {
    position: absolute;
    left: 304px;
    top: 359px;
    width: 58px;
    height: 58px;
    background: var(--navy);
  }
  .brand-name {
    position: absolute;
    left: 156px;
    top: 427px;
    margin: 0;
    font-family: "Questrial", sans-serif;
    font-size: 34px;
    font-weight: 400;
    line-height: 1;
    letter-spacing: 0.015em;
    color: var(--navy);
    white-space: nowrap;
  }
  .brand-rule {
    position: absolute;
    left: 157px;
    top: 476px;
    width: 237px;
    height: 2px;
    background: var(--navy);
  }
  .person-name {
    position: absolute;
    left: 396px;
    top: 540px;
    margin: 0;
    font-family: "Cinzel", serif;
    font-size: 53px;
    font-weight: 400;
    line-height: 1;
    letter-spacing: 0.02em;
    color: var(--navy);
    white-space: nowrap;
  }
  .contact {
    position: absolute;
    left: 395px;
    top: 624px;
    margin: 0;
    padding: 0;
    list-style: none;
    font-family: "Libre Baskerville", serif;
    font-size: 18px;
    line-height: 38px;
    letter-spacing: 0.2em;
    color: var(--ink);
    white-space: nowrap;
  }
  .contact .web {
    color: var(--navy);
  }
  .footer-rule {
    position: absolute;
    left: 394px;
    top: 799px;
    width: 684px;
    height: 2px;
    background: var(--navy);
  }
</style>
</head>
<body>
<main class="canvas">
  <section class="card"></section>
  <div class="brand-mark"></div>
  <p class="brand-name">FERNLOW ADVISORY</p>
  <div class="brand-rule"></div>
  <h1 class="person-name">Daniel Whitcombe</h1>
  <ul class="contact">
    <li class="email">dan@fernlowadvisory.com</li>
    <li class="street">2837 North 9th Avenue, Summit Floor</li>
    <li class="city">Cedar Hollow, Westland 60483</li>
    <li class="web">www.fernlowadvisory.com</li>
  </ul>
  <div class="footer-rule"></div>
</main>
</body>
</html>
```